Business Card Design

We are a new residential construction company.our team is made up of young highly skilled tradesman of the next generation of carpenters coming through with new skills and ideas.we chose the name meridian as it means strikingly different from the rest as this is what we plan to be and we would like to portray this in our business card.we like Bold lettering as we want to make a statement, also the use of colour would be great as we want to stand out from the usual plain construction cards and logos.
I have attached a logo sketch I did as a rough idea if you can tidy it up or improve on it would be good.
I have also attached the LBP logo please include this on the card small but still legible.
open to any colourschemes ideas.
thanks
(note)please delete the LBP#804317 off from the card details please.
Industry/Entity Type
Construction
Contact Information for Business Card
MERIDIAN CONSTRUCTION LIMITED
Director:Tom Halvick
Mobile :0217364820
Email:Meridian.Construction@quillpost.example
Address:48 Wendle place,Ashgrove park 2091,Auckland
LBP#BP804317

```html
<!DOCTYPE html>
<html lang="en">
<head>
<meta charset="UTF-8">
<title>Meridian Construction – Business Card</title>
<link rel="stylesheet" href="https://fonts.googleapis.com/css2?family=Roboto:wght@400;700&display=swap">
<style>
  :root {
    --page-bg: #f2f2f2;
    --card-dark: #0c0d10;
    --card-mid: #1b1d22;
    --rule-blue: #2f5fe0;
    --rule-glow: rgba(70, 120, 255, 0.55);
    --name-blue: #3d55c9;
    --icon-blue: #5a6fd6;
    --text-light: #eef0f4;
    --text-muted: #c9ccd3;
    --divider: #7c808a;
    --logo-silver: #d9dde4;
    --badge-fill: #3b4252;
  }
  * { margin: 0; padding: 0; box-sizing: border-box; }
  html, body {
    width: 1200px;
    height: 900px;
    overflow: hidden;
    background: var(--page-bg);
    font-family: "Roboto", Arial, sans-serif;
  }
  .canvas {
    position: relative;
    width: 1200px;
    height: 900px;
  }
  .business-card {
    position: absolute;
    left: 100px;
    top: 165px;
    width: 1000px;
    height: 570px;
    border-radius: 44px;
    overflow: hidden;
    background:
      radial-gradient(ellipse at 50% 30%, var(--card-mid) 0%, var(--card-dark) 70%);
    box-shadow: 0 18px 40px rgba(0, 0, 0, 0.28);
  }
  .brand {
    position: absolute;
    top: 70px;
    left: 0;
    width: 100%;
    text-align: center;
    color: var(--logo-silver);
    font-weight: 700;
    text-transform: uppercase;
    line-height: 1;
  }
  .brand-primary {
    display: block;
    font-size: 96px;
    letter-spacing: 6px;
  }
  .brand-secondary {
    display: block;
    margin-top: 12px;
    font-size: 70px;
    letter-spacing: 4px;
  }
  .accent-rule {
    position: absolute;
    left: 0;
    top: 288px;
    width: 100%;
    height: 5px;
    background: linear-gradient(90deg, rgba(47,95,224,0.4), var(--rule-blue) 30%, var(--rule-blue) 70%, rgba(47,95,224,0.4));
    box-shadow: 0 0 14px 3px var(--rule-glow);
  }
  .person {
    position: absolute;
    top: 362px;
    right: 640px;
    text-align right;
    text-align: right;
  }
  .person-name {
    color: var(--name-blue);
    font-size: 31px;
    font-weight: 400;
    letter-spacing: 0.5px;
  }
  .person-title {
    margin-top: 8px;
    color: var(--text-muted);
    font-size: 26px;
  }
  .column-divider {
    position: absolute;
    left: 385px;
    top: 348px;
    width: 2px;
    height: 150px;
    background: var(--divider);
  }
  .contact-list {
    position: absolute;
    left: 408px;
    top: 350px;
    list-style: none;
    color: var(--text-light);
    font-size: 25px;
    line-height: 37px;
    white-space: nowrap;
  }
  .contact-item {
    display: flex;
    align-items: center;
    gap: 10px;
  }
  .contact-icon {
    width: 24px;
    height: 24px;
    flex: none;
    fill: var(--icon-blue);
  }
  .licence-badge {
    position: absolute;
    right: 48px;
    bottom: 40px;
    width: 56px;
    height: 56px;
    border-radius: 50%;
    background: var(--badge-fill);
  }
</style>
</head>
<body>
<main class="canvas">
  <section class="business-card">
    <h1 class="brand">
      <span class="brand-primary">Meridian</span>
      <span class="brand-secondary">Construction</span>
    </h1>

    <div class="accent-rule"></div>

    <div class="person">
      <p class="person-name">Tom Halvick</p>
      <p class="person-title">Director</p>
    </div>

    <div class="column-divider"></div>

    <ul class="contact-list">
      <li class="contact-item">
        <svg class="contact-icon" viewBox="0 0 24 24" aria-hidden="true">
          <path d="M6.6 10.8a15.1 15.1 0 0 0 6.6 6.6l2.2-2.2a1 1 0 0 1 1-.25 11.4 11.4 0 0 0 3.6.57 1 1 0 0 1 1 1V20a1 1 0 0 1-1 1A17 17 0 0 1 3 4a1 1 0 0 1 1-1h3.5a1 1 0 0 1 1 1c0 1.25.2 2.45.57 3.57a1 1 0 0 1-.25 1z"/>
        </svg>
        <span>0217364820</span>
      </li>
      <li class="contact-item">
        <svg class="contact-icon" viewBox="0 0 24 24" aria-hidden="true">
          <path d="M2 6a2 2 0 0 1 2-2h16a2 2 0 0 1 2 2v12a2 2 0 0 1-2 2H4a2 2 0 0 1-2-2zm2 .5V7l8 5 8-5v-.5z"/>
        </svg>
        <span>Meridian.Construction@quillpost.example</span>
      </li>
      <li class="contact-item">
        <svg class="contact-icon" viewBox="0 0 24 24" aria-hidden="true">
          <path d="M12 3 2 12h3v8h5v-6h4v6h5v-8h3z"/>
        </svg>
        <span>48 Wendle place,Ashgrove park</span>
      </li>
      <li class="contact-item">
        <span>2091,Auckland</span>
      </li>
    </ul>

    <div class="licence-badge" role="img" aria-label="Licensed building practitioner badge"></div>
  </section>
</main>
</body>
</html>
```